Guiding the Evergreen Young Competitor:
A Family Roadmap for Nurturing Bold, Steady, and Resilient Daughters on Fields and Beyond.
📘 Book Cover Design Brief – “Guiding the Evergreen Young Competitor”

Project Title:
Design a bold, inspiring book cover for a best-selling book titled:
Guiding the Evergreen Young Competitor
Subtitle: A Family Roadmap for Nurturing Bold, Steady, and Resilient Daughters on Fields and Beyond

🎯 Audience:

Parents of female athletes ages 14–20 who want their daughters to build confidence, strength, resilience, and long-term success both in sports and in life.

This book should feel encouraging, empowering, and credible — NOT cheesy, childish, or overly academic.

📕 Design Tone & Style:

Powerful and professional — should feel like a best-selling book from a leading performance or parenting expert

Emotionally compelling — conveys hope, resilience, strength, and possibility

Visually modern and clean — avoid anything overly busy, cliché, or childish

Heroic/aspirational tone — think transformation, leadership, strong positioning

💡 Visual Direction / Ideas (Use as Inspiration, Not Limitation):

Strong, confident teenage female athlete imagery — adaptable beyond one specific sport

Symbolic visuals — e.g. athlete standing strong, on a starting line, looking bold into the future, silhouette, or power stance

Bold typography that feels clean and modern (e.g., Proxima Nova, Montserrat, Gotham, Bebas Neue, etc.)

A title that stands out clearly when viewed as a thumbnail on Bookvale

Color tones: Empowering, modern, and strong: think deep blues, greens, purples, or golds — avoid playful pastels or overly girly themes

Potential imagery: textured backgrounds, motion, bravery, development, strength, growth, sport/action overlays

🔥 What the Cover MUST Communicate:

✅ This is for parents who want strong, confident female athletes
✅ It’s a guidebook for personal development AND sports performance
✅ It’s about creating “UNSHAKEABLE” confidence — physically, mentally and emotionally
✅ The message is: You can help your daughter become her strongest, most confident self

📚 Back-of-Book Summary (for context):

"Guiding the Evergreen Young Competitor" is a parent's blueprint to building girls who are strong in body, confident in mind, and ready to lead on and off the field. Through simple strategies around strength training, mindset, nutrition, and character development, this book gives parents the tools to help their daughters stay injury-resistant, break through mental barriers, and unlock their full potential — in sports and in life.

✅ Deliverables:

Full cover design (front, back, spine) for paperback
High-resolution files (print-ready)
Source files (PSD, AI, etc.)
3D mockup versions of the book (standing, flat, stack)

Target Market(s)

Industry/Entity Type

Fitness

Font styles to use
Sans Serif

Colors
FFF300
FFF600
FEFA6F
FFFEC7
FFFEE8

Requirements
Must have
• Bold Font
Should not have
• I don't want an image of a female athlete. I want this to be font based.

```html
<!DOCTYPE html>
<html lang="en">
<head>
<meta charset="utf-8">
<title>Guiding the Evergreen Young Competitor – Full Cover</title>
<link rel="stylesheet" href="https://fonts.googleapis.com/css2?family=Bebas+Neue&family=Oswald:wght@200;300&display=swap">
<style>
  :root {
    --gold: #f8dc78;
    --gold-bright: #fde27e;
    --white: #ffffff;
    --night: #0d1522;
    --dusk: #3a4a5e;
    --horizon: #6f7d8c;
    --sun: #fff1b8;
    --ground: #020203;
    --barcode-panel: #ffffff;
  }
  * { margin: 0; padding: 0; box-sizing: border-box; }
  html, body { width: 1200px; height: 854px; overflow: hidden; background: var(--ground); }

  .cover {
    position: relative;
    width: 1200px;
    height: 854px;
    overflow: hidden;
    font-family: "Bebas Neue", "Oswald", sans-serif;
  }

  .scenery {
    position: absolute;
    inset: 0;
    background:
      radial-gradient(ellipse 120px 90px at 909px 425px, var(--sun) 0%, rgba(255,225,140,0.75) 35%, rgba(255,200,110,0) 100%),
      radial-gradient(ellipse 520px 200px at 880px 470px, rgba(214,170,90,0.55) 0%, rgba(120,110,100,0.25) 50%, rgba(0,0,0,0) 100%),
      linear-gradient(to bottom,
        var(--night) 0%,
        #18243a 25%,
        var(--dusk) 45%,
        var(--horizon) 55%,
        #3b3b3a 58%,
        #101012 68%,
        var(--ground) 80%,
        var(--ground) 100%);
  }

  /* Back cover */
  .back-blurb {
    position: absolute;
    left: 101px;
    top: 156px;
    width: 371px;
    color: var(--gold);
    font-size: 16.2px;
    line-height: 23.1px;
    text-align: justify;
    text-align-last: left;
    letter-spacing: 0.2px;
  }
  .author-photo {
    position: absolute;
    left: 222px;
    top: 344px;
    width: 134px;
    height: 166px;
    border: 2px solid var(--gold);
    background: radial-gradient(ellipse at 50% 40%, #4a3e38 0%, #1a1a1c 60%, #0c0c0d 100%);
  }
  .author-bio {
    position: absolute;
    left: 101px;
    top: 521px;
    width: 371px;
    color: var(--gold);
    font-size: 13.6px;
    line-height: 18.4px;
    text-align: justify;
    text-align-last: left;
    letter-spacing: 0.15px;
  }
  .barcode-panel {
    position: absolute;
    left: 315px;
    top: 685px;
    width: 195px;
    height: 105px;
    background: var(--barcode-panel);
  }

  /* Spine */
  .spine-title, .spine-author {
    position: absolute;
    left: 600px;
    color: var(--gold-bright);
    white-space: nowrap;
    transform-origin: center center;
    transform: translate(-50%, -50%) rotate(90deg);
  }
  .spine-title { top: 326px; font-size: 22.5px; letter-spacing: 0.2px; }
  .spine-author { top: 626px; font-size: 30px; letter-spacing: 0.5px; }

  /* Front cover */
  .front-title {
    position: absolute;
    left: 700px;
    top: 92px;
    width: 420px;
    text-align: center;
    color: var(--gold-bright);
  }
  .front-title .lead {
    display: block;
    font-family: "Oswald", sans-serif;
    font-weight: 200;
    font-size: 58px;
    line-height: 64px;
    letter-spacing: 0.5px;
  }
  .front-title .main {
    display: block;
    font-size: 76px;
    line-height: 74px;
    letter-spacing: 0.5px;
    text-shadow: 0 2px 6px rgba(0,0,0,0.35);
  }
  .front-title .main.wide { font-size: 94px; line-height: 84px; }

  .front-subtitle {
    position: absolute;
    left: 770px;
    top: 574px;
    width: 284px;
    text-align: center;
    color: var(--white);
  }
  .front-subtitle span { display: block; }
  .front-subtitle .s1 { font-size: 37px; line-height: 36px; }
  .front-subtitle .s2 { font-size: 34px; line-height: 36px; }
  .front-subtitle .s3 { font-size: 30px; line-height: 34px; }
  .front-subtitle .s4 { font-size: 22px; line-height: 28px; }

  .front-author {
    position: absolute;
    left: 730px;
    top: 742px;
    width: 360px;
    text-align: center;
    color: var(--gold-bright);
    font-size: 52px;
    line-height: 52px;
    letter-spacing: 0.5px;
  }
</style>
</head>
<body>
  <div class="cover">
    <div class="scenery" role="img" aria-label="Photographic backdrop: starry night sky fading to a golden sunrise over a distant horizon, with a dark hilltop along the bottom"></div>

    <section class="back-cover">
      <p class="back-blurb">"Guiding the Evergreen Young Competitor" is a parent's blueprint to building girls who are strong in body, confident in mind, and ready to lead on and off the field. Through simple strategies around strength training, mindset, nutrition, and character development, this book gives parents the tools to help their daughters stay injury-resistant, break through mental barriers, and unlock their full potential — in sports and in life.</p>

      <div class="author-photo" role="img" aria-label="Author portrait: Dorian Wexley in a dark Stride Works t-shirt"></div>

      <p class="author-bio">Dorian has 15 years experience, specializing in personal training and sport performance. He focuses his training on creating programs that improve performance and reduce the risk of injury. Dorian has worked with clients from 8 – 73. He is a 2 time Bookvale best-selling author with Rise Every Day and Peak Fuel for Teen Competitors. Dorian commits his life to coaching each client to be great. Stride Works was born out of his passion to make each person who walks in the door the very best version of themselves.</p>

      <div class="barcode-panel"></div>
    </section>

    <section class="spine">
      <span class="spine-title">GUIDING THE EVERGREEN YOUNG COMPETITOR</span>
      <span class="spine-author">DORIAN WEXLEY</span>
    </section>

    <section class="front-cover">
      <h1 class="front-title">
        <span class="lead">GUIDING THE</span>
        <span class="main">EVERGREEN YOUNG</span>
        <span class="main wide">COMPETITOR</span>
      </h1>

      <h2 class="front-subtitle">
        <span class="s1">A FAMILY ROADMAP</span>
        <span class="s2">FOR NURTURING BOLD,</span>
        <span class="s3">STEADY, AND RESILIENT</span>
        <span class="s4">DAUGHTERS ON FIELDS AND BEYOND</span>
      </h2>

      <p class="front-author">DORIAN WEXLEY</p>
    </section>
  </div>
</body>
</html>
```